business card with 2 locations on 1 card

I need a modern looking business card that I would use at 2 different locations. Possibly 1 location on 1 side and other location on other side. One should be able to distinguish the 2 locations immediately before having to read the address or description on card. You can take a look at my website to see what I'm drawn to. The logo is brand new that I just purchased on Craft Hive. I want to emphasize family.
Updates

Let's not use the yellow and blue colors. Added Thursday, August 31, 2017

Target Market(s)

women and children

Industry/Entity Type

Health And Wellness

Contact Information for Business Card

Business name: Willow Brook Chiropractic & Acupuncture
My name: Lorin Daske
Job title: DC, MAOM, LAc (CA), CNS

Location 1
Address: 4817 Marlowe Blvd, Suite B-100, Frisco, TX 75034
Phone: (469) 555-0182
Fax: (972) 555-0137

Location 2
Address: 1936 Belvane Road, Suite 100, Plano, TX 75075
Phone: (469) 555-0169
Fax: (972) 555-0137

Email: drlorindaske@mailnest.example
Website: www.drlorindaske.example

Font styles to use
Serif
Sans Serif

Colors

Designer to choose colors to be used in the design.

Requirements
Must have
• distinction between 2 locations.
Nice to have
• Colors preference below is there. But I like to see what you come up with too!

```html
<!DOCTYPE html>
<html lang="en">
<head>
<meta charset="utf-8">
<title>Willow Brook Chiropractic &amp; Acupuncture — Business Card</title>
<link rel="stylesheet" href="https://fonts.googleapis.com/css2?family=Source+Sans+3:wght@400;600&display=swap">
<style>
  :root {
    --backdrop: #2a2a2a;
    --card-light: #ececec;
    --card-dark: #1c1c1c;
    --teal: #2b6a65;
    --leaf-green: #3f9a4c;
    --ink: #2e2e2e;
    --silver: #cfcfcf;
    --silver-soft: #9c9c9c;
  }
  * { box-sizing: border-box; margin: 0; padding: 0; }
  html, body {
    width: 1200px; height: 600px; overflow: hidden;
    background: var(--backdrop);
    font-family: "Source Sans 3", "Segoe UI", Arial, sans-serif;
  }
  .canvas { position: relative; width: 1200px; height: 600px; }

  .card {
    position: absolute; top: 140px;
    width: 550px; height: 320px;
    border-radius: 18px;
  }
  .card--front { left: 35px; background: var(--card-light); color: var(--ink); }
  .card--back  { left: 615px; background: var(--card-dark); color: var(--silver); }

  /* Front: holder */
  .holder { position: absolute; left: 28px; top: 18px; padding-left: 14px; border-left: 8px solid var(--teal); }
  .holder__name { font-size: 24px; line-height: 28px; font-weight: 400; color: var(--ink); letter-spacing: -0.3px; }
  .holder__title { font-size: 14px; line-height: 18px; color: var(--leaf-green); }

  /* Brand name block */
  .brand { position: absolute; text-align: center; font-weight: 600; text-transform: uppercase; }
  .brand__mark { display: block; margin: 0 auto; border-radius: 50%; }
  .brand__name { display: block; letter-spacing: 1px; }
  .brand__tagline { display: block; letter-spacing: 0.6px; }

  .brand--front { right: 22px; top: 16px; width: 200px; color: var(--teal); }
  .brand--front .brand__mark { width: 76px; height: 76px; background: var(--teal); }
  .brand--front .brand__name { font-size: 22px; line-height: 24px; margin-top: 10px; }
  .brand--front .brand__tagline { font-size: 9px; line-height: 12px; }

  .brand--back { left: 0; right: 0; top: 68px; color: var(--silver); }
  .brand--back .brand__mark { width: 130px; height: 130px; border: 4px solid var(--silver); }
  .brand--back .brand__name { font-size: 34px; line-height: 38px; margin-top: 12px; letter-spacing: 1.5px; }
  .brand--back .brand__tagline { font-size: 12px; line-height: 16px; }
  .website { position: absolute; left: 0; right: 0; top: 258px; text-align: center; font-size: 12px; color: var(--silver-soft); }

  /* Locations */
  .location { position: absolute; top: 186px; list-style: none; font-size: 14.5px; line-height: 17px; color: var(--ink); }
  .location--frisco { left: 26px; }
  .location--plano { right: 26px; text-align: right; }
  .location li { display: flex; align-items: flex-start; gap: 8px; margin-bottom: 9px; }
  .location li.address { margin-bottom: 12px; }
  .location--plano li { flex-direction: row-reverse; }
  .icon { flex: none; width: 16px; height: 16px; fill: var(--teal); margin-top: 1px; }
</style>
</head>
<body>
<main class="canvas">

  <section class="card card--front" aria-label="Card front">
    <div class="holder">
      <p class="holder__name">Dalen Morrow</p>
      <p class="holder__title">Director</p>
    </div>

    <div class="brand brand--front">
      <span class="brand__mark"></span>
      <span class="brand__name">Willow Brook</span>
      <span class="brand__tagline">Chiropractic &amp; Acupuncture</span>
    </div>

    <ul class="location location--frisco">
      <li class="address">
        <svg class="icon" viewBox="0 0 16 16"><path d="M8 0a5.5 5.5 0 0 0-5.5 5.5C2.5 9.6 8 16 8 16s5.5-6.4 5.5-10.5A5.5 5.5 0 0 0 8 0zm0 7.8a2.3 2.3 0 1 1 0-4.6 2.3 2.3 0 0 1 0 4.6z"/></svg>
        <span>4817 Marlowe Blvd,<br>Suite B-100, Frisco, TX 75034</span>
      </li>
      <li>
        <svg class="icon" viewBox="0 0 16 16"><path d="M1 5.5C1 3.5 4 2.5 8 2.5s7 1 7 3v1.5h-3.5V5.2h-7V7H1z"/><path d="M3.5 8.5 5.5 6h5l2 2.5V14h-9z"/></svg>
        <span>(469) 555-0182</span>
      </li>
      <li>
        <svg class="icon" viewBox="0 0 16 16"><path d="M4 1h6l2 2v4H4z"/><rect x="1" y="6" width="3" height="9" rx="1"/><path d="M5 8h10v7H5zm2 2v1h2v-1zm3 0v1h2v-1zm-3 2v1h2v-1zm3 0v1h2v-1z"/></svg>
        <span>(972) 555-0137</span>
      </li>
      <li>
        <svg class="icon" viewBox="0 0 16 16"><path d="M1 4h14v1L8 9.5 1 5z"/><path d="M1 6.3 8 11l7-4.7V13H1z"/></svg>
        <span>drlorindaske@mailnest.example</span>
      </li>
    </ul>

    <ul class="location location--plano">
      <li class="address">
        <svg class="icon" viewBox="0 0 16 16"><path d="M8 0a5.5 5.5 0 0 0-5.5 5.5C2.5 9.6 8 16 8 16s5.5-6.4 5.5-10.5A5.5 5.5 0 0 0 8 0zm0 7.8a2.3 2.3 0 1 1 0-4.6 2.3 2.3 0 0 1 0 4.6z"/></svg>
        <span>1936 Belvane Road, Suite 100<br>Plano, TX 75075</span>
      </li>
      <li>
        <svg class="icon" viewBox="0 0 16 16"><path d="M1 5.5C1 3.5 4 2.5 8 2.5s7 1 7 3v1.5h-3.5V5.2h-7V7H1z"/><path d="M3.5 8.5 5.5 6h5l2 2.5V14h-9z"/></svg>
        <span>(469) 555-0169</span>
      </li>
      <li>
        <svg class="icon" viewBox="0 0 16 16"><path d="M4 1h6l2 2v4H4z"/><rect x="1" y="6" width="3" height="9" rx="1"/><path d="M5 8h10v7H5zm2 2v1h2v-1zm3 0v1h2v-1zm-3 2v1h2v-1zm3 0v1h2v-1z"/></svg>
        <span>(972) 555-0137</span>
      </li>
      <li>
        <svg class="icon" viewBox="0 0 16 16"><path d="M1 4h14v1L8 9.5 1 5z"/><path d="M1 6.3 8 11l7-4.7V13H1z"/></svg>
        <span>drlorindaske@mailnest.example</span>
      </li>
    </ul>
  </section>

  <section class="card card--back" aria-label="Card back">
    <div class="brand brand--back">
      <span class="brand__mark"></span>
      <span class="brand__name">Willow Brook</span>
      <span class="brand__tagline">Chiropractic &amp; Acupuncture</span>
    </div>
    <p class="website">www.drlorindaske.example</p>
  </section>

</main>
</body>
</html>
```